【重要事項】
ワードプレスでのホームページ制作依頼、別途予定あり
デザインから制作まで一貫して行える方はご相談ください。
トップページデザインのみのご提案ももちろん大歓迎です。

【トップページデザインの要望】
・コンパクトでユーザーフレンドリー、お客様を意識したトップページ
サイトを訪れた人が求める情報にすぐアクセスできるデザインを希望します。詳細は添付ファイルをご覧ください。

【弊社ホームページ】
リニューアル対象のホームページURLのほか下記
http://rokugaen-shop.jp/
園芸のECサイトです。

【添付ファイル】
共有事項は添付ファイルにまとめています。お手数ですがご一読ください。
ロゴもございます。デザイン作成にお役立てください。
http://rokugaen.jp/
1ページ
緑系
• 高解像度JPG (.jpg)
• PNG形式 (.png)
8/31追記(質問への回答まとめ)

【納品形式の追加】
ai形式/PSD形式の納品可
※要望には個別でも柔軟に対応します。

【ロゴデータの追加】
pngデータ2つ、jpgデータ1つ
色のこだわりは強くありません。デザインに合わせてご活用ください。

【参考にしたいサイト】
https://q-m.co.jp/
最近できた会社様で、お客様目線に振り切ったデザインです。
ここまでポップにはできませんが、取り入れられる要素は取り入れたいと思っています。

https://www.nuvo-greno.com/
競合他社様ですが、多言語対応できるデザインレイアウトが印象的です。
弊社も英語対応のホームページ(弊社にて文言を翻訳)にする予定です。

みなさまのご応募お待ちしております。

当選者:桐山様
当選理由:社内会議による選考の末、多数決により決定しました。
色合いとデザインの段組が非常に優れておりました。
次点入選:blinker様、ree様
入選理由:blnker様は社内会議で最後まで当選作品と一、二を争う優秀作品でした。
特にイラストのテイストが社長の好みに合っており好印象でした。
ree様は写真の選定センス、全体のデザイン感が女性社員に受けました。

今回は担当が変わってから初めての提案でした。
不慣れなことが多い中、たくさんのご提案をいただき、様々な改善点や面白いデザイン、よりよいHPづくりのヒントをランサーのエキスパートの皆様よりいただきました。
誠にお礼申し上げます。

また、後半ご提出のご提案には、逐一ご挨拶ができず申し訳ございませんでした。
今回いただけた縁を活かして、よりよいHP制作につなげていきたいと考えております。

惜しくも当選、入選とならなかった皆様にも、心よりお礼を申し上げます。
またの機会がございましたら、よろしくお願いします。

```html
<!DOCTYPE html>
<html lang="ja">
<head>
<meta charset="utf-8">
<title>RokuGaEn</title>
<link href="https://fonts.googleapis.com/css2?family=M+PLUS+Rounded+1c:wght@400;700;800&display=swap" rel="stylesheet">
<style>
:root{
  --green:#2f9a5b;
  --green-dark:#23804a;
  --green-pale:#eef6ef;
  --yellow:#f6d43c;
  --yellow-pale:#fdf6cf;
  --orange:#f29a1f;
  --ink:#3b3b3b;
  --grey:#8a8a8a;
  --white:#ffffff;
}
*{margin:0;padding:0;box-sizing:border-box}
html,body{width:1200px;height:3528px;overflow:hidden}
body{font-family:"M PLUS Rounded 1c",sans-serif;color:var(--ink);background:var(--white);position:relative}
.abs{position:absolute}
.ph{position:absolute;overflow:hidden}

/* header */
.site-header{position:absolute;top:0;left:0;width:1200px;height:80px;z-index:5}
.brand{position:absolute;left:220px;top:18px;color:var(--white);font-weight:800;font-size:26px;letter-spacing:1px}
.brand small{display:block;font-size:9px;font-weight:400;letter-spacing:3px;text-align:center}
.global-nav{position:absolute;left:470px;top:0;width:540px;height:62px;background:var(--white);border-radius:0 0 18px 18px;display:flex;justify-content:space-around;align-items:center}
.global-nav a{text-decoration:none;color:var(--ink);font-size:13px;font-weight:700;text-align:center;line-height:1.3}
.global-nav a span{display:block;font-size:9px;color:var(--green);font-weight:400}
.header-icons{position:absolute;right:30px;top:8px;display:flex;flex-direction:column;gap:8px}
.header-icons span{width:46px;height:46px;border-radius:50%;display:flex;align-items:center;justify-content:center}
.header-icons .i1{background:#8cc63f}
.header-icons .i2{background:var(--orange)}

/* hero */
.hero-top{left:0;top:0;width:1200px;height:640px;background:linear-gradient(180deg,#5e7f4a 0%,#8fb069 40%,#6a8c50 70%,#3c4f31 100%)}
.hero-bottom{left:0;top:600px;width:1200px;height:650px;background:linear-gradient(180deg,#c9dfe8 0%,#dfe9d4 35%,#9dbb72 65%,#6d8f47 100%)}
.hero-copy{position:absolute;left:0;width:1200px;top:282px;text-align:center;color:var(--white);font-size:28px;font-weight:700;letter-spacing:4px;text-shadow:0 2px 6px rgba(0,0,0,.35)}
.about-blob{position:absolute;left:180px;top:580px}
.about-body{position:absolute;left:265px;top:680px;width:370px}
.about-body h2{color:var(--green);font-size:26px;font-weight:800;margin-bottom:30px}
.about-body p{font-size:12px;line-height:2;color:var(--grey)}
.circle-btn{position:absolute;border-radius:50%;display:flex;align-items:center;justify-content:center;color:var(--white);font-size:13px;font-weight:700;text-align:center;line-height:1.4}
.btn-about{left:545px;top:920px;width:112px;height:112px;background:var(--yellow)}
.btn-company{left:415px;top:1035px;width:112px;height:112px;background:var(--orange)}

/* target banners */
.target{position:absolute;top:1252px;width:560px;height:168px;border-radius:8px;overflow:hidden}
.target.livestock{left:28px;background:linear-gradient(120deg,#5a4632,#8b7658 50%,#c9b99b)}
.target.garden{left:612px;background:linear-gradient(120deg,#6e5a3e,#93a05c 50%,#c8c9a0)}
.target-label{position:absolute;left:0;top:0;width:100%;height:100%;display:flex;align-items:center;justify-content:center;color:var(--white);font-size:19px;font-weight:800;line-height:1.5;text-align:center;background:rgba(0,0,0,.25)}
.target-arrow{display:inline-flex;width:30px;height:30px;border-radius:50%;background:var(--white);margin-left:14px;align-items:center;justify-content:center}

/* section headings */
.sec-title{position:absolute;left:0;width:1200px;text-align:center;color:var(--green);font-size:24px;font-weight:800;letter-spacing:3px}
.sec-title small{display:block;font-size:10px;letter-spacing:2px;color:var(--grey);font-weight:400;margin-top:4px}
.sec-title::after{content:"";display:block;width:30px;height:3px;background:var(--yellow);margin:10px auto 0;border-radius:2px}

/* news */
.news{position:absolute;left:240px;top:1625px;width:345px}
.tab{display:inline-block;background:var(--yellow);color:var(--white);font-size:13px;font-weight:700;padding:8px 26px;border-radius:6px 6px 0 0}
.news-list{list-style:none;border-top:3px solid var(--yellow)}
.news-list li{display:flex;gap:16px;font-size:12px;padding:20px 14px;border-bottom:1px dashed #d9d9d9}
.news-list li time{color:var(--grey)}
.news-list li.pick{background:var(--yellow-pale)}
.insta{position:absolute;left:625px;top:1620px;width:335px;height:370px;border:3px solid var(--yellow);border-radius:6px;padding:16px 22px}
.insta h3{text-align:center;color:var(--yellow);font-size:14px;font-weight:700;margin-bottom:14px}
.insta-grid{display:grid;grid-template-columns:repeat(3,90px);gap:8px;justify-content:center}
.insta-grid div{width:90px;height:90px;border-radius:3px;background:linear-gradient(135deg,#5c8d3a,#9cc46a 60%,#c75b3a)}

/* staff */
.staff-bg{position:absolute;left:0;top:2100px}
.staff-photo{position:absolute;top:2310px;width:230px;height:130px;border:4px solid var(--yellow);background:linear-gradient(180deg,#d9d6cf,#3c3c42 60%,#26262b)}
.staff-tag{position:absolute;top:-4px;left:50%;transform:translateX(-50%);background:var(--yellow);color:var(--white);font-size:10px;font-weight:700;padding:3px 12px;white-space:nowrap}
.recruit-photo{left:228px;top:2470px;width:340px;height:220px;border-radius:6px;background:linear-gradient(120deg,#e7e2d8,#b9b2a8 40%,#3a3a40 80%)}
.recruit-blob{position:absolute;left:560px;top:2480px}
.recruit-text{position:absolute;left:600px;top:2520px;width:150px;color:var(--white);text-align:center}
.recruit-text h3{font-size:18px;font-weight:800}
.recruit-text h3 small{display:block;font-size:9px;font-weight:400}
.recruit-text p{font-size:10px;line-height:1.8;margin-top:10px}
.btn-recruit{left:790px;top:2585px;width:92px;height:92px;background:var(--yellow);font-size:11px}

/* contact */
.contact-box{position:absolute;top:2950px;width:225px;height:120px;border:2px solid var(--yellow);border-radius:6px;text-align:center;padding-top:14px}
.contact-box .lead{font-size:9px;color:var(--grey);line-height:1.5}
.contact-box .main{font-size:22px;font-weight:800;color:var(--green);margin:6px 0 4px;display:flex;align-items:center;justify-content:center;gap:6px}
.contact-box .note{font-size:9px;color:var(--grey)}
.tree{position:absolute}

/* footer */
.footer-wave{position:absolute;left:0;top:3100px}
.footer{position:absolute;left:0;top:3190px;width:1200px;height:338px;background:var(--green);color:var(--white)}
.footer .brand-f{position:absolute;left:230px;top:28px;font-size:28px;font-weight:800}
.footer .brand-f small{display:block;font-size:9px;font-weight:400;letter-spacing:3px}
.footer address{position:absolute;left:230px;top:100px;font-style:normal;font-size:10px;line-height:1.8}
.footer .brand-box{position:absolute;left:230px;top:170px;width:150px;height:46px;background:var(--green-dark);border-radius:4px;display:flex;align-items:center;justify-content:center;font-weight:800;font-size:17px}
.sitemap{position:absolute;left:470px;top:40px;display:flex;gap:34px;font-size:11px}
.sitemap ul{list-style:none;line-height:2}
.sitemap li.head{font-weight:700}
.sitemap li.sub{padding-left:10px;opacity:.9}
.copy{position:absolute;left:0;bottom:16px;width:1200px;text-align:center;font-size:9px;opacity:.85}
</style>
</head>
<body>

<!-- hero imagery -->
<div class="ph hero-top" role="img" aria-label="Child feeding a cow at a farm fence"></div>
<div class="ph hero-bottom" role="img" aria-label="Parent lifting a child in a green farm field"></div>

<header class="site-header">
  <div class="brand">RokuGaEn<small>六雅園</small></div>
  <nav class="global-nav">
    <a href="#">六雅園について<span>ABOUT</span></a>
    <a href="#">六雅園の取り扱い<span>PRODUCTS</span></a>
    <a href="#">六雅園で働く人々<span>PEOPLE</span></a>
    <a href="#">採用情報<span>RECRUIT</span></a>
    <a href="#">会社概要<span>COMPANY</span></a>
  </nav>
  <div class="header-icons">
    <span class="i1"><svg width="20" height="20" viewBox="0 0 24 24" fill="#fff"><path d="M6.6 10.8a15 15 0 0 0 6.6 6.6l2.2-2.2c.3-.3.7-.4 1-.2 1.1.4 2.3.6 3.6.6.6 0 1 .4 1 1V20c0 .6-.4 1-1 1A17 17 0 0 1 3 4c0-.6.4-1 1-1h3.5c.6 0 1 .4 1 1 0 1.3.2 2.5.6 3.6.1.3 0 .7-.2 1z"/></svg></span>
    <span class="i2"><svg width="20" height="20" viewBox="0 0 24 24" fill="none" stroke="#fff" stroke-width="2"><rect x="3" y="5" width="18" height="14" rx="2"/><path d="M3 7l9 6 9-6"/></svg></span>
  </div>
</header>

<p class="hero-copy">動物や植物と過ごす豊かな生活を。</p>

<svg class="about-blob" width="520" height="600" viewBox="0 0 520 600">
  <path d="M70 60 C150 -10 380 -10 460 70 C530 150 510 300 490 390 C460 520 330 590 220 570 C100 550 20 470 10 340 C0 220 10 120 70 60 Z" fill="#fff"/>
</svg>
<div class="about-body">
  <h2>私たちについて</h2>
  <p>テキストが入ります。テキストが入ります。テキストが入ります。テキストが入ります。テキストが入ります。テキストが入ります。テキストが入ります。テキストが入ります。テキストが入ります。テキストが入ります。テキストが入ります。テキストが入ります。テキストが入ります。テキストが入ります。テキストが入ります。テキストが入ります。</p>
</div>
<a class="circle-btn btn-about">六雅園について<br>›</a>
<a class="circle-btn btn-company">会社概要<br>›</a>

<svg class="abs" style="left:0;top:1180px" width="1200" height="70" viewBox="0 0 1200 70" preserveAspectRatio="none">
  <path d="M0 40 C200 0 400 60 600 30 C800 0 1000 50 1200 20 L1200 70 L0 70 Z" fill="#fff"/>
</svg>

<a class="target livestock" role="img" aria-label="Cows in a livestock barn">
  <span class="target-label">牛・豚・鶏・犬猫など<br>畜産専門のお客様<span class="target-arrow"><svg width="12" height="12" viewBox="0 0 12 12"><path d="M4 2l4 4-4 4" stroke="#2f9a5b" stroke-width="2" fill="none"/></svg></span></span>
</a>
<a class="target garden" role="img" aria-label="Gardening tools and potted plants on soil">
  <span class="target-label">農業・園芸の<br>商品をお求めのお客様<span class="target-arrow"><svg width="12" height="12" viewBox="0 0 12 12"><path d="M4 2l4 4-4 4" stroke="#2f9a5b" stroke-width="2" fill="none"/></svg></span></span>
</a>

<!-- news -->
<h2 class="sec-title" style="top:1500px">お知らせ<small>NEWS</small></h2>
<section class="news">
  <span class="tab">新着情報</span>
  <ul class="news-list">
    <li class="pick"><time>2017.08.31</time>新商品のお知らせを掲載しました</li>
    <li><time>2017.08.24</time>夏季休業日のご案内を掲載しました</li>
    <li><time>2017.08.10</time>展示会出展のお知らせを掲載しました</li>
    <li><time>2017.07.28</time>採用情報を更新しました</li>
    <li><time>2017.07.14</time>ホームページを公開しました</li>
  </ul>
</section>
<section class="insta">
  <h3>インスタグラム</h3>
  <div class="insta-grid" role="img" aria-label="Grid of vegetable and plant photos">
    <div></div><div></div><div></div><div></div><div></div><div></div><div></div><div></div><div></div>
  </div>
</section>

<!-- staff -->
<svg class="staff-bg" width="1200" height="720" viewBox="0 0 1200 720" preserveAspectRatio="none">
  <path d="M0 80 C300 0 900 0 1200 80 L1200 720 L0 720 Z" fill="#eef6ef"/>
</svg>
<h2 class="sec-title" style="top:2205px">六雅園で働く人々<small>PEOPLE</small></h2>
<div class="staff-photo" style="left:228px" role="img" aria-label="Group of staff members in suits"><span class="staff-tag">営業部</span></div>
<div class="staff-photo" style="left:485px" role="img" aria-label="Group of staff members in suits"><span class="staff-tag">管理部</span></div>
<div class="staff-photo" style="left:742px" role="img" aria-label="Group of staff members in suits"><span class="staff-tag">物流部</span></div>
<div class="ph recruit-photo" role="img" aria-label="Staff members in office attire"></div>
<svg class="recruit-blob" width="240" height="220" viewBox="0 0 240 220">
  <path d="M40 20 C100 -5 200 0 225 60 C245 120 220 190 150 210 C80 225 15 190 5 120 C-3 70 10 35 40 20 Z" fill="#2f9a5b"/>
</svg>
<div class="recruit-text">
  <h3>採用情報<small>RECRUIT</small></h3>
  <p>一緒に働く仲間を募集しています。詳しい情報はこちらからご覧ください。</p>
</div>
<a class="circle-btn btn-recruit">詳しくは<br>こちら ›</a>

<!-- contact -->
<h2 class="sec-title" style="top:2850px">お問い合わせ<small>CONTACT</small></h2>
<div class="contact-box" style="left:228px">
  <p class="lead">ご質問・ご相談はこちらの<br>フォームよりお送りください</p>
  <p class="main"><svg width="22" height="22" viewBox="0 0 24 24" fill="none" stroke="#2f9a5b" stroke-width="2"><rect x="3" y="5" width="18" height="14" rx="2"/><path d="M3 7l9 6 9-6"/></svg>メールフォーム ›</p>
  <p class="note">24時間受付しております</p>
</div>
<div class="contact-box" style="left:486px">
  <p class="lead">畜産関連の商品に関する<br>お問い合わせはこちら</p>
  <p class="main"><svg width="20" height="20" viewBox="0 0 24 24" fill="#2f9a5b"><path d="M6.6 10.8a15 15 0 0 0 6.6 6.6l2.2-2.2c.3-.3.7-.4 1-.2 1.1.4 2.3.6 3.6.6.6 0 1 .4 1 1V20c0 .6-.4 1-1 1A17 17 0 0 1 3 4c0-.6.4-1 1-1h3.5c.6 0 1 .4 1 1 0 1.3.2 2.5.6 3.6.1.3 0 .7-.2 1z"/></svg>0123-45-6780</p>
  <p class="note">受付 平日 9:00〜17:00</p>
</div>
<div class="contact-box" style="left:744px">
  <p class="lead">農業・園芸の商品に関する<br>お問い合わせはこちら</p>
  <p class="main"><svg width="20" height="20" viewBox="0 0 24 24" fill="#2f9a5b"><path d="M6.6 10.8a15 15 0 0 0 6.6 6.6l2.2-2.2c.3-.3.7-.4 1-.2 1.1.4 2.3.6 3.6.6.6 0 1 .4 1 1V20c0 .6-.4 1-1 1A17 17 0 0 1 3 4c0-.6.4-1 1-1h3.5c.6 0 1 .4 1 1 0 1.3.2 2.5.6 3.6.1.3 0 .7-.2 1z"/></svg>0123-45-6789</p>
  <p class="note">受付 平日 9:00〜17:00</p>
</div>

<div class="tree" style="left:70px;top:3080px;width:90px;height:110px;background:linear-gradient(180deg,#7cc04a,#2f9a5b);border-radius:45px 45px 10px 10px" role="img" aria-label="Tree illustration"></div>
<div class="tree" style="left:1010px;top:3110px;width:150px;height:80px;background:linear-gradient(180deg,#7cc04a,#2f9a5b);border-radius:40px 40px 8px 8px" role="img" aria-label="Trees and grazing animals illustration"></div>

<!-- footer -->
<svg class="footer-wave" width="1200" height="100" viewBox="0 0 1200 100" preserveAspectRatio="none">
  <path d="M0 70 C250 20 450 50 650 40 C850 30 1000 60 1200 50 L1200 100 L0 100 Z" fill="#2f9a5b"/>
</svg>
<footer class="footer">
  <div class="brand-f">RokuGaEn<small>六雅園</small></div>
  <address>〒000-0000 サンプル県サンプル市1-2-3<br>TEL 0123-45-6780<br>FAX 0123-45-6781</address>
  <div class="brand-box">RokuGaEn</div>
  <div class="sitemap">
    <ul><li class="head">六雅園について</li></ul>
    <ul><li class="head">六雅園の取り扱い</li><li class="sub">畜産関連の商品</li><li class="sub">農業・園芸の商品</li></ul>
    <ul><li class="head">六雅園で働く人々</li><li class="sub">営業部</li><li class="sub">管理部</li><li class="sub">物流部</li></ul>
    <ul><li class="head">採用情報</li></ul>
    <ul><li class="head">会社概要</li><li class="sub">代表挨拶</li><li class="sub">沿革</li><li class="sub">アクセス</li></ul>
  </div>
  <p class="copy">Copyright © ROKUGAEN. All rights reserved.</p>
</footer>

</body>
</html>
```